Hollowbrook Yard Services - Needs a business card! Easy JOB!

I need a business card for a new company called Hollowbrook Yard Services. I will be offering the below services.

I am relatively open for ideas, so please be at your creative best.

I think I will list all the services offered on the rear of the card.

- Gardening
- Lawn Care
- Hedge Trimming
- Rubbish Removal
- Weeding/Spraying
- Landscaping
- Gutter Cleaning
- Solar Panel Cleaning
- Irrigation
- Pruning
- On-Site Mulching
- Ask for other services

I am still a little undecided on the colours. I prefer the logos with the Blue text, but I am open for ideas ( the logo/texts colours are not final).

Please use the catch phrase "What can Hollowbrook do for you?"

Here are the required details.

Hollowbrook Yard Services

Miles Fenwarick (owner)
Ph: 1300 555 014
Mob: 0400 555 286

miles@hollowbrookyard.com.au
www.hollowbrookyard.com.au
chatterly.com/HollowbrookYard
quipster.com/HollowbrookYard
ABN: 555 019 472 ( this can be in smaller text somewhere, this is the least important )

Thankyou in advance! And good luck.

regards,
Miles
Updates

Hi everyone, please make sure you include the phrase "What can Hollowbrook do for you?" on the designs.

thanks,
Miles

Definitely liking the focus on a majority of the design on the blue colour from the logo. Also a splash of green in the plant.

Please make sure you list the services provided on the rear of the card. thanks.

With the service listing, please make "ask for other services" stand out, either a different colour or position or size... as long as it is more noticeable than the other services listed. Thanks.

Industry/Entity Type

Business

Requirements
Must have
• - use the font supplied (Brandon Family Font)
- use of the catch phrase "What can Hollowbrook do for you?"
- Double sided design
- Chatterly and Quipster logos/links
- Please use symbol/picture for "phone" "mobile" "email" instead of using the words.
- List the services provided on the rear of the card

```html
<!DOCTYPE html>
<html lang="en">
<head>
<meta charset="utf-8">
<title>Hollowbrook Yard Services – Business Card</title>
<link href="https://fonts.googleapis.com/css2?family=Josefin+Sans:wght@400;600;700&display=swap" rel="stylesheet">
<style>
  :root {
    --blue-light: #1c9ae0;
    --blue-mid: #2370c4;
    --blue-deep: #2d3a97;
    --green: #8dc63f;
    --ink: #2b4597;
    --grey: #6b6f7a;
    --white: #ffffff;
    --shadow: rgba(0,0,0,0.28);
  }
  * { margin: 0; padding: 0; box-sizing: border-box; }
  html, body { width: 1200px; height: 927px; overflow: hidden; background: var(--white); }
  body { position: relative; font-family: "Josefin Sans", sans-serif; }

  .card {
    position: absolute; top: 68px; width: 333px; height: 583px;
    border-radius: 16px; overflow: hidden; background: var(--white);
    box-shadow: 3px 4px 7px var(--shadow);
  }
  .card--front { left: 205px; }
  .card--back { left: 632px; }

  /* front */
  .front-brand {
    height: 253px; display: flex; flex-direction: column; align-items: center;
    background: linear-gradient(180deg, var(--blue-light) 0%, var(--blue-mid) 45%, var(--blue-deep) 100%);
    padding-top: 30px; color: var(--white); font-weight: 700; text-align: center;
  }
  .brand-mark { width: 74px; height: 74px; border-radius: 50%; background: var(--green); margin-bottom: 38px; }
  .brand-name { font-size: 34px; line-height: 1; letter-spacing: 0; white-space: nowrap; }
  .brand-sub { font-size: 16px; letter-spacing: 1px; margin-top: 7px; }

  .name-bar {
    height: 40px; background: var(--green); color: var(--white);
    font-weight: 700; font-size: 20px; letter-spacing: 0.5px;
    display: flex; align-items: center; justify-content: center; padding-top: 4px;
  }
  .role { text-align: center; color: var(--green); font-size: 19px; margin-top: 12px; }

  .contacts { list-style: none; margin: 16px 0 0 22px; }
  .contacts li {
    display: flex; align-items: center; height: 34px;
    color: var(--ink); font-size: 17px; white-space: nowrap;
  }
  .contacts svg, .contacts .social-square { width: 24px; height: 24px; margin-right: 9px; flex: none; }
  .social-square { background: var(--blue-deep); border-radius: 3px; }

  .web-bar {
    position: absolute; left: 0; bottom: 0; width: 100%; height: 63px;
    background: linear-gradient(180deg, var(--blue-mid), var(--blue-deep));
    color: var(--white); font-weight: 700; font-size: 22px;
    display: flex; align-items: center; justify-content: center; padding-top: 4px;
  }

  /* back */
  .tagline {
    margin-top: 35px; height: 82px;
    background: linear-gradient(180deg, var(--blue-light), var(--blue-deep));
    color: var(--white); font-weight: 700; font-size: 21px; line-height: 1.3;
    text-align: center; display: flex; flex-direction: column; justify-content: center; padding-top: 5px;
    white-space: nowrap;
  }
  .tagline .accent { color: var(--green); }
  .services { list-style: none; margin: 22px 0 0 28px; }
  .services li {
    display: flex; align-items: center; height: 30.4px;
    color: var(--blue-mid); font-size: 22px; white-space: nowrap;
  }
  .services li.services__extra { color: var(--green); }
  .services svg { width: 18px; height: 12px; margin-right: 16px; flex: none; }
  .abn { position: absolute; left: 27px; bottom: 26px; font-size: 15px; color: var(--grey); }

  /* presentation band */
  .brand-band {
    position: absolute; left: 0; top: 706px; width: 1200px; height: 165px;
    background: linear-gradient(180deg, var(--blue-light) 0%, var(--blue-mid) 50%, var(--blue-deep) 100%);
    display: flex; flex-direction: column; align-items: center; padding-top: 18px;
    color: var(--white); font-weight: 700; text-align: center;
  }
  .brand-band .brand-mark { width: 56px; height: 56px; margin-bottom: 20px; }
  .brand-band .brand-name { font-size: 32px; }
  .brand-band .brand-sub { font-size: 13px; margin-top: 4px; }
</style>
</head>
<body>

<section class="card card--front" aria-label="Business card front">
  <header class="front-brand">
    <div class="brand-mark"></div>
    <div class="brand-name">HOLLOWBROOK</div>
    <div class="brand-sub">YARD SERVICES</div>
  </header>
  <div class="name-bar">MILES FENWARICK</div>
  <p class="role">Owner</p>
  <ul class="contacts">
    <li>
      <svg viewBox="0 0 24 24" aria-label="Phone"><path fill="#2d3a97" d="M3 8c0-3 4-5 9-5s9 2 9 5l-1 2-4-1V7c-2-1-6-1-8 0v2l-4 1zM6 12l2-2h8l2 2 2 8H4z"/><circle cx="12" cy="15" r="2.5" fill="#fff"/></svg>
      1300 555 014
    </li>
    <li>
      <svg viewBox="0 0 24 24" aria-label="Mobile"><rect x="7" y="1" width="10" height="22" rx="2" fill="#2d3a97"/><rect x="9" y="4" width="6" height="7" fill="#fff"/><rect x="9" y="13" width="6" height="7" fill="#fff" opacity=".5"/></svg>
      0400 555 286
    </li>
    <li>
      <svg viewBox="0 0 24 24" aria-label="Email"><rect x="2" y="5" width="20" height="14" rx="1" fill="#2d3a97"/><path d="M3 6l9 7 9-7" stroke="#fff" stroke-width="1.6" fill="none"/></svg>
      miles@hollowbrookyard.com.au
    </li>
    <li><span class="social-square" aria-hidden="true"></span>chatterly.com/HollowbrookYard</li>
    <li><span class="social-square" aria-hidden="true"></span>quipster.com/HollowbrookYard</li>
  </ul>
  <footer class="web-bar">hollowbrookyard.com.au</footer>
</section>

<section class="card card--back" aria-label="Business card back">
  <h2 class="tagline">
    <span>WHAT CAN <span class="accent">HOLLOWBROOK</span></span>
    <span>DO FOR YOU?</span>
  </h2>
  <svg width="0" height="0" style="position:absolute">
    <defs><path id="leaf" d="M1 10C3 3 10 0 17 2 14 9 8 12 1 10z"/></defs>
  </svg>
  <ul class="services">
    <li><svg viewBox="0 0 18 12"><use href="#leaf" fill="#8dc63f"/></svg>Gardening</li>
    <li><svg viewBox="0 0 18 12"><use href="#leaf" fill="#8dc63f"/></svg>Lawn Care</li>
    <li><svg viewBox="0 0 18 12"><use href="#leaf" fill="#8dc63f"/></svg>Hedge Trimming</li>
    <li><svg viewBox="0 0 18 12"><use href="#leaf" fill="#8dc63f"/></svg>Rubbish Removal</li>
    <li><svg viewBox="0 0 18 12"><use href="#leaf" fill="#8dc63f"/></svg>Weeding/Spraying</li>
    <li><svg viewBox="0 0 18 12"><use href="#leaf" fill="#8dc63f"/></svg>Landscaping</li>
    <li><svg viewBox="0 0 18 12"><use href="#leaf" fill="#8dc63f"/></svg>Gutter Cleaning</li>
    <li><svg viewBox="0 0 18 12"><use href="#leaf" fill="#8dc63f"/></svg>Solar Panel Cleaning</li>
    <li><svg viewBox="0 0 18 12"><use href="#leaf" fill="#8dc63f"/></svg>Irrigation</li>
    <li><svg viewBox="0 0 18 12"><use href="#leaf" fill="#8dc63f"/></svg>Pruning</li>
    <li><svg viewBox="0 0 18 12"><use href="#leaf" fill="#8dc63f"/></svg>On-Site Mulching</li>
    <li class="services__extra"><svg viewBox="0 0 18 12"><use href="#leaf" fill="#8dc63f"/></svg>Ask for Other Services</li>
  </ul>
  <p class="abn">ABN: 555 019 472</p>
</section>

<section class="brand-band" aria-label="Brand banner">
  <div class="brand-mark"></div>
  <div class="brand-name">HOLLOWBROOK</div>
  <div class="brand-sub">YARD SERVICES</div>
</section>

</body>
</html>
```